Modern business card and stationary for a dental office
World Class Care
Professional
Dr. Gavin Morrow
General Dentist
4836- 92 Street S.E. Edmonton, AB T6K 3R2
drmorrow@pinehollowdental.ca
pinehollowdental.ca
Family Clinic *Cosmetic Dentistry *Implant Dentistry *services provided by a general dentist

```html
<!DOCTYPE html>
<html lang="en">
<head>
<meta charset="UTF-8">
<title>Pine Hollow Dental – Business Cards</title>
<link href="https://fonts.googleapis.com/css2?family=Open+Sans:wght@400;600;700&display=swap" rel="stylesheet">
<style>
  :root {
    --bg: #8c8c8c;
    --card: #ffffff;
    --navy: #1d3f73;
    --deep-blue: #1f4f8f;
    --sky: #2a9fe0;
    --ice: #bfe4f7;
    --ink: #2f3a4a;
  }
  * { box-sizing: border-box; margin: 0; padding: 0; }
  html, body { width: 1200px; height: 908px; overflow: hidden; }
  body {
    background: var(--bg);
    font-family: "Open Sans", Arial, sans-serif;
    position: relative;
  }
  .card {
    position: absolute;
    top: 299px;
    width: 540px;
    height: 310px;
    background: var(--card);
    border-radius: 14px;
    overflow: hidden;
    box-shadow: 0 6px 18px rgba(0,0,0,0.25);
  }
  .card--services { left: 40px; }
  .card--contact { left: 620px; }
  .card svg.decor { position: absolute; inset: 0; }

  .feature-art {
    position: absolute;
    left: 250px;
    top: 24px;
    width: 290px;
    height: 150px;
    border-radius: 10px 0 0 10px;
    background: linear-gradient(135deg, #dff1fb 0%, #6fbbe9 55%, #1f4f8f 100%);
  }

  .services {
    position: absolute;
    left: 40px;
    top: 190px;
  }
  .services__title {
    font-weight: 700;
    font-size: 17px;
    color: var(--navy);
    margin-bottom: 4px;
  }
  .services__list { list-style: none; }
  .services__list li {
    font-size: 14px;
    color: var(--sky);
    line-height: 1.35;
  }
  .services__list li::before { content: "\2022"; margin-right: 4px; }

  .dentist {
    position: absolute;
    right: 36px;
    top: 140px;
    text-align: right;
  }
  .dentist__name { font-weight: 700; font-size: 19px; color: var(--navy); }
  .dentist__role { font-size: 14px; color: var(--sky); }

  .brand {
    position: absolute;
    left: 34px;
    top: 150px;
    display: flex;
    align-items: center;
    gap: 8px;
  }
  .brand__dot { width: 14px; height: 14px; border-radius: 50%; background: var(--deep-blue); }
  .brand__name { font-weight: 600; font-size: 17px; color: var(--deep-blue); letter-spacing: 0.5px; }

  .contact {
    position: absolute;
    left: 36px;
    top: 190px;
    font-size: 11.5px;
    color: var(--ink);
    line-height: 1.45;
  }
  .contact__row { display: flex; align-items: center; gap: 6px; }
  .contact__icon { width: 12px; height: 12px; flex: none; }
</style>
</head>
<body>

  <section class="card card--services">
    <div class="feature-art" role="img" aria-label="Large clinic brand artwork in blue tones"></div>
    <div class="services">
      <h2 class="services__title">Family Clinic</h2>
      <ul class="services__list">
        <li>Cosmetic Dentistry</li>
        <li>Implant Dentistry</li>
        <li>Services Provided by a General Dentist</li>
      </ul>
    </div>
  </section>

  <section class="card card--contact">
    <svg class="decor" viewBox="0 0 540 310" aria-hidden="true">
      <defs>
        <linearGradient id="bandDeep" x1="0" y1="0" x2="1" y2="1">
          <stop offset="0" stop-color="#3b7cc4"/>
          <stop offset="1" stop-color="#173a6e"/>
        </linearGradient>
      </defs>
      <path d="M150,0 H540 V92 C470,70 420,112 340,106 C270,100 220,40 150,0 Z" fill="url(#bandDeep)"/>
      <path d="M120,0 C200,50 260,112 340,118 C420,124 470,84 540,104" fill="none" stroke="#2a9fe0" stroke-width="6"/>
      <path d="M100,0 C190,62 250,126 340,130 C420,134 475,100 540,116" fill="none" stroke="#bfe4f7" stroke-width="3"/>
    </svg>

    <div class="dentist">
      <div class="dentist__name">Dr. Gavin Morrow</div>
      <div class="dentist__role">General Dentist</div>
    </div>

    <div class="brand">
      <span class="brand__dot"></span>
      <span class="brand__name">PINE HOLLOW DENTAL</span>
    </div>

    <div class="contact">
      <div>4836- 92 Street S.E.</div>
      <div>Edmonton, AB T6K 3R2</div>
      <div class="contact__row">
        <svg class="contact__icon" viewBox="0 0 12 12"><circle cx="6" cy="6" r="6" fill="#2a9fe0"/><path d="M4,3 L5,3 L5.6,4.6 L5,5.2 C5.4,6 6,6.6 6.8,7 L7.4,6.4 L9,7 L9,8 C6,8.4 3.6,6 4,3 Z" fill="#fff"/></svg>
        <span>780-555-0142</span>
      </div>
      <div class="contact__row">
        <svg class="contact__icon" viewBox="0 0 12 12"><circle cx="6" cy="6" r="6" fill="#2a9fe0"/><rect x="3.5" y="4" width="5" height="4.5" fill="#fff"/><rect x="4.5" y="2.8" width="3" height="1.6" fill="#fff"/></svg>
        <span>780-555-0178</span>
      </div>
      <div class="contact__row">
        <svg class="contact__icon" viewBox="0 0 12 12"><circle cx="6" cy="6" r="6" fill="#2a9fe0"/><rect x="3" y="4" width="6" height="4.2" fill="#fff"/><path d="M3,4 L6,6.3 L9,4" fill="none" stroke="#2a9fe0" stroke-width="0.8"/></svg>
        <span>drmorrow@pinehollowdental.ca</span>
      </div>
      <div class="contact__row">
        <svg class="contact__icon" viewBox="0 0 12 12"><circle cx="6" cy="6" r="6" fill="#2a9fe0"/><circle cx="6" cy="6" r="3.2" fill="none" stroke="#fff" stroke-width="0.8"/><path d="M2.8,6 H9.2 M6,2.8 C4.6,4.5 4.6,7.5 6,9.2 M6,2.8 C7.4,4.5 7.4,7.5 6,9.2" fill="none" stroke="#fff" stroke-width="0.7"/></svg>
        <span>pinehollowdental.ca</span>
      </div>
    </div>
  </section>

</body>
</html>
```